Business Card Design Project

I run holistic health workshops, speaking engagements, group and 1on1 coaching, cooking classes, and am a speaker and presenter on holistic health topics.

I would like professionally designed business cards using the attached logo. I would like the reverse of the cards to use the leaf pattern blown up large across the back of the card as the design. I'd also like to use the words "mind.body.spirit.nutrition" across the backside of the cards.

The front of the cards should contain the following contact details:
Megan Thorsby-Kell
Founder & President
The Harwick Advisory Group
+61 477 392 604
theharwickadvisorygroup@mailbrook.example

Target Market(s)

Corporate HR, Health & wellness businesses, upmarket spas, other businesses in the holistic health & wellness fields looking for a speaker/presenter/workshop leader

Industry/Entity Type

Cooking

Requirements
Must have
• Must use the attached design; must use earth tones in line with the logo (browns/greens/blues/tans)

```html
<!DOCTYPE html>
<html lang="en">
<head>
<meta charset="utf-8">
<title>The Harwick Advisory Group — Business Card</title>
<link rel="stylesheet" href="https://fonts.googleapis.com/css2?family=Arimo:wght@400;700&family=Didact+Gothic&display=swap">
<style>
  :root {
    --card-white: #ffffff;
    --brand-lime: #84ec24;
    --brand-charcoal: #3b463d;
    --text-on-lime: #ffffff;
  }
  * { margin: 0; padding: 0; box-sizing: border-box; }
  html, body {
    width: 1200px;
    height: 720px;
    overflow: hidden;
    background: var(--card-white);
  }
  .card {
    position: relative;
    width: 1200px;
    height: 720px;
    background: var(--card-white);
  }
  .brand {
    position: absolute;
    left: 82px;
    top: 280px;
    width: 480px;
    display: flex;
    align-items: center;
    gap: 24px;
  }
  .brand__dot {
    flex: none;
    width: 68px;
    height: 68px;
    border-radius: 50%;
    background: var(--brand-lime);
  }
  .brand__name {
    font-family: "Didact Gothic", sans-serif;
    font-size: 48px;
    line-height: 1.12;
    color: var(--brand-charcoal);
  }
  .contact-panel {
    position: absolute;
    left: 594px;
    top: 0;
    width: 606px;
    height: 720px;
    background: var(--brand-lime);
  }
  .contact {
    position: absolute;
    right: 81px;
    top: 320px;
    text-align: right;
    color: var(--text-on-lime);
    white-space: nowrap;
  }
  .contact__name {
    font-family: "Arimo", sans-serif;
    font-weight: 700;
    font-size: 43px;
    line-height: 1.1;
  }
  .contact__role {
    font-family: "Didact Gothic", sans-serif;
    font-size: 35px;
    line-height: 1.15;
  }
  .contact__phone {
    font-family: "Arimo", sans-serif;
    font-weight: 700;
    font-size: 43px;
    line-height: 1.1;
    margin-top: 49px;
  }
  .contact__email {
    font-family: "Arimo", sans-serif;
    font-size: 22px;
    line-height: 1.2;
    margin-top: 9px;
  }
  .contact__email strong { font-weight: 700; }
</style>
</head>
<body>
  <main class="card">
    <div class="brand">
      <span class="brand__dot" aria-hidden="true"></span>
      <p class="brand__name">The Harwick<br>Advisory Group</p>
    </div>
    <section class="contact-panel">
      <div class="contact">
        <p class="contact__name">Megan Thorsby-Kell</p>
        <p class="contact__role">Founder &amp; President</p>
        <p class="contact__phone">+61 477 392 604</p>
        <p class="contact__email"><strong>theharwickadvisorygroup</strong>@mailbrook.example</p>
      </div>
    </section>
  </main>
</body>
</html>
```